Boutique Recruiting Firm Needs Eye-Catching Business Cards (and potentially new logo)!

I run a recruiting company in Charleston, South Carolina. I have a ton of networking events coming up and need business cards to grab potential clients attention.

I currently have a logo but if you want to try and recreate the logo to something more modern I am open to that. If you do decide to create a new logo please submit the business card with the old logo and the new one.

Staffing Under Blue Lanterns, LLC is the name of my company. I create videos to my clients and candidates which allows me to standout from my competition so I would like a business card (and possibly new logo) to do the same.

I do not specialize in any one industry of recruiting.

```html
<!DOCTYPE html>
<html lang="en">
<head>
<meta charset="utf-8">
<title>Staffing Under Blue Lanterns, LLC — Business Card</title>
<link rel="stylesheet" href="https://fonts.googleapis.com/css2?family=Roboto:wght@400;500;700&display=swap">
<style>
  :root {
    --card-bg: #ffffff;
    --page-bg: #ffffff;
    --brand-blue: #2c4f8f;
    --ink-dark: #333333;
    --ink-text: #3a3a3a;
    --card-edge: #e2e2e2;
  }
  html, body {
    margin: 0;
    padding: 0;
    width: 1200px;
    height: 706px;
    overflow: hidden;
    background: var(--page-bg);
  }
  .business-card {
    position: relative;
    width: 1200px;
    height: 706px;
    box-sizing: border-box;
    border: 1px solid var(--card-edge);
    background: var(--card-bg);
    font-family: "Roboto", Arial, sans-serif;
    color: var(--ink-text);
  }
  .brand-mark {
    position: absolute;
    left: 70px;
    top: 200px;
    width: 420px;
    display: flex;
    flex-direction: column;
    align-items: center;
    gap: 30px;
  }
  .brand-square {
    flex: none;
    width: 130px;
    height: 130px;
    background: var(--brand-blue);
  }
  .brand-name {
    margin: 0;
    font-size: 46px;
    font-weight: 700;
    line-height: 1.15;
    text-align: center;
    color: var(--brand-blue);
  }
  .divider {
    position: absolute;
    left: 533px;
    top: 110px;
    width: 2px;
    height: 486px;
    background: var(--ink-dark);
  }
  .person {
    position: absolute;
    left: 599px;
    top: 104px;
  }
  .person-name {
    margin: 0;
    font-size: 41px;
    font-weight: 700;
    color: var(--ink-dark);
    letter-spacing: 0.3px;
  }
  .person-title {
    margin: 8px 0 0;
    font-size: 27px;
    font-weight: 400;
    color: var(--ink-dark);
  }
  .contact-list {
    position: absolute;
    left: 596px;
    top: 350px;
    margin: 0;
    padding: 0;
    list-style: none;
  }
  .contact-item {
    position: relative;
    height: 51px;
    padding-left: 72px;
    font-size: 28px;
    line-height: 51px;
    letter-spacing: 0.6px;
    color: var(--ink-text);
    white-space: nowrap;
  }
  .contact-icon {
    position: absolute;
    left: 0;
    top: 6px;
    width: 38px;
    height: 40px;
  }
</style>
</head>
<body>
  <main class="business-card">
    <div class="brand-mark">
      <span class="brand-square"></span>
      <p class="brand-name">Staffing Under<br>Blue Lanterns, LLC</p>
    </div>

    <div class="divider"></div>

    <header class="person">
      <h1 class="person-name">Rohan Mehtani</h1>
      <p class="person-title">Managing Director</p>
    </header>

    <ul class="contact-list">
      <li class="contact-item">
        <svg class="contact-icon" viewBox="0 0 38 40" aria-hidden="true">
          <path d="M19 2 C10 2 4 8.5 4 16.5 C4 26 19 38 19 38 C19 38 34 26 34 16.5 C34 8.5 28 2 19 2 Z" fill="var(--ink-dark)"/>
          <circle cx="19" cy="16" r="5.5" fill="var(--card-bg)"/>
        </svg>
        48 Meeting Street, Charleston, SC
      </li>
      <li class="contact-item">
        <svg class="contact-icon" viewBox="0 0 38 40" aria-hidden="true">
          <circle cx="19" cy="20" r="16" fill="none" stroke="var(--ink-dark)" stroke-width="2.4"/>
          <path d="M13.5 11.5 l4 0.5 l1 5 l-2.5 1.8 c1.3 3 3 4.8 6 6.2 l1.8 -2.5 l5 1 l0.5 4 c-1 1.5 -3 2 -4.5 1.8 c-6.5 -1.3 -11.8 -6.6 -12.8 -13 c-0.2 -1.8 0.4 -3.8 1.5 -4.8 Z" fill="var(--ink-dark)"/>
        </svg>
        +1 843 555 0147
      </li>
      <li class="contact-item">hello@bluelanternsllc.com</li>
      <li class="contact-item">www.staffingbluelanterns.com</li>
      <li class="contact-item">linkup.com/bluelanternsllc</li>
    </ul>
  </main>
</body>
</html>
```